Creative, fresh business card design for Orrin Linings

We need a fresh, creative business card design for Orrin Linings. We are the manufacturer of Orrin Linings in Australia. Wall panels are 2400 x 1200mm panels made from MDF and feature 3D patterns on the face of the panel. The colours to be used are green, silver/grey and white RGB
Red 187
Green 207
Blue 65.

An idea is to possibly use a watermark of one of our designs as a background (like on the "Ferns" design on the left hand side of page 2 of our brochure).

Target Market(s)

Interior designers, architects, builders and home renovators

Industry/Entity Type

Business

Contact Information for Business Card

Details to go on the card are:
Our logo (attached),
Slogan: "Decorative panels for interiors and exteriors",
Contact name,
Position,
Mobile phone number,
Business address,
Business phone,
Business fax,
Website and
Email address.

I have attached a few images of our panels and our brochure for reference.

The colours of the business card should feature our logo colours which are: RGB
Red 187
Green 207
Blue 65

Requirements
Must have
• Very modern fonts and design. Some of the designs shown especially the "Weave" design which is a popular design.
Nice to have
• Creative but simple design. Very contemporary.
Should not have
• Anything ornate or old fashioned.

```html
<!DOCTYPE html>
<html lang="en">
<head>
<meta charset="utf-8">
<title>Orrin Linings – Business Card</title>
<link href="https://fonts.googleapis.com/css2?family=Arimo:wght@400;700&display=swap" rel="stylesheet">
<style>
  :root {
    --brand-green: rgb(187, 207, 65);
    --slate: #8c8c8e;
    --slate-light: #a5a5a7;
    --paper: #ffffff;
    --backdrop: #ececec;
    --panel-dark: #5c5d60;
    --panel-mid: #9a9b9e;
    --rule: #9b9b9b;
  }
  * { box-sizing: border-box; margin: 0; padding: 0; }
  html, body {
    width: 1200px;
    height: 987px;
    overflow: hidden;
    background: var(--backdrop);
    font-family: "Arimo", Arial, sans-serif;
  }
  .card {
    position: absolute;
    left: 293px;
    width: 615px;
    height: 350px;
    background: var(--paper);
    box-shadow: 0 2px 6px rgba(0,0,0,0.18);
    overflow: hidden;
  }
  .card--front { top: 131px; }
  .card--back { top: 506px; }

  .brand {
    position: absolute;
    display: flex;
    flex-direction: column;
    align-items: center;
  }
  .brand__lockup {
    display: flex;
    align-items: center;
    gap: 12px;
  }
  .brand__square {
    width: 34px;
    height: 34px;
    background: var(--brand-green);
  }
  .brand__name {
    font-size: 34px;
    font-weight: 400;
    color: var(--slate);
    letter-spacing: 0.5px;
    white-space: nowrap;
  }
  .brand__tagline {
    margin-top: 12px;
    font-size: 12.5px;
    line-height: 15px;
    letter-spacing: 2.4px;
    color: var(--slate-light);
    text-align: center;
  }

  .card--front .brand {
    left: 0;
    right: 0;
    top: 62px;
  }
  .holder {
    position: absolute;
    top: 204px;
    left: 0;
    right: 0;
    text-align: center;
    font-size: 15px;
    color: var(--slate);
  }
  .holder__name {
    font-size: 20px;
    font-weight: 700;
    color: var(--brand-green);
    letter-spacing: 0.3px;
  }
  .holder__role { margin-left: 2px; }
  .front__rule {
    position: absolute;
    top: 244px;
    left: 0;
    right: 0;
    height: 2px;
    background: var(--rule);
  }
  .contact-band {
    position: absolute;
    top: 246px;
    left: 0;
    right: 0;
    bottom: 0;
    background: var(--brand-green);
    color: var(--paper);
    text-align: center;
    font-size: 15px;
    line-height: 25px;
    padding-top: 12px;
  }
  .contact-band b { font-weight: 700; }

  .panel-photo {
    position: absolute;
    top: 0;
    left: 0;
    width: 345px;
    height: 100%;
    background: linear-gradient(90deg,
      var(--panel-dark) 0%,
      var(--panel-mid) 45%,
      #d8dadc 70%,
      var(--paper) 100%);
  }
  .card--back .brand {
    left: 290px;
    width: 250px;
    top: 122px;
  }
  .card--back .brand__name { font-size: 30px; }
  .card--back .brand__square { width: 30px; height: 30px; }
</style>
</head>
<body>

<section class="card card--front" aria-label="Business card front">
  <div class="brand">
    <div class="brand__lockup">
      <span class="brand__square"></span>
      <span class="brand__name">Orrin Linings</span>
    </div>
    <p class="brand__tagline">decorative panels for<br>interiors &amp; landscapes</p>
  </div>

  <p class="holder">
    <span class="holder__name">DARA WHITLOW -</span>
    <span class="holder__role">CEO&amp;Founder</span>
  </p>

  <div class="front__rule"></div>

  <div class="contact-band">
    <p>412 Tallow Street, Geelong, Victoria 3220</p>
    <p><b>P :</b> (03) 5521 7840 &nbsp;<b>F :</b> (03) 5521 7841</p>
    <p>dwhitlow@orrinlinings.com | www.orrinlinings.com</p>
  </div>
</section>

<section class="card card--back" aria-label="Business card back">
  <div class="panel-photo" role="img" aria-label="Photograph of a grey wave-patterned 3D wall panel beside a staircase, fading into a bright interior"></div>

  <div class="brand">
    <div class="brand__lockup">
      <span class="brand__square"></span>
      <span class="brand__name">Orrin Linings</span>
    </div>
    <p class="brand__tagline">decorative panels for<br>interiors &amp; landscapes</p>
  </div>
</section>

</body>
</html>
```